Harrows Menu Design for a sports bar concept

We need an updated look for this current menu design, 8.5x16". It's a sports bar concept. We like the wood planks at the top header but need to do something with the white space.

Target Market(s)

ages 20-40s. Social drinkers.

Industry/Entity Type

Sports Bar

Font styles to use
Sans Serif

Colors
f58b49
3176b5
0355a3
ec1f27

Requirements
Must have
• Cannot change logo.
Nice to have
• Similar fonts if possible.
• Titles: Asphaltum WF
• Descriptions: Akzidenz Grotesk Roman

```html
<!DOCTYPE html>
<html lang="en">
<head>
<meta charset="utf-8">
<title>Harrows Grill Menu</title>
<link rel="stylesheet" href="https://fonts.googleapis.com/css2?family=Oswald:wght@500;700&family=Roboto+Condensed:wght@400;700&family=Kalam:wght@400&display=swap">
<style>
:root{
  --orange:#f58b49;
  --blue:#3176b5;
  --navy:#0355a3;
  --red:#ec1f27;
  --ink:#1f2430;
  --muted:#5b6170;
  --paper:#fbfbfd;
  --wood-dark:#5a3a22;
  --wood-light:#9a6a42;
}
*{box-sizing:border-box;margin:0;padding:0}
html,body{width:1200px;height:2256px;overflow:hidden}
body{background:var(--paper);font-family:"Roboto Condensed",Arial,sans-serif;color:var(--ink);position:relative}
.menu{position:relative;width:1200px;height:2256px;background:linear-gradient(180deg,#ffffff 0%,#f3f6fb 50%,#fdf3ec 100%)}
.header{position:absolute;left:0;top:0;width:1200px;height:380px;display:flex;align-items:center;justify-content:center}
.wood{position:absolute;inset:0;background:linear-gradient(180deg,var(--wood-light) 0%,var(--wood-dark) 55%,#7b5233 100%)}
.brand{position:relative;text-align:center;font-family:"Oswald",Arial,sans-serif;font-weight:700;color:#ffffff;text-transform:uppercase;line-height:.95}
.brand .name{display:block;font-size:150px;letter-spacing:4px}
.brand .sub{display:block;font-size:64px;letter-spacing:10px}
.section-title{position:absolute;left:0;width:1200px;height:70px;display:flex;align-items:center}
.section-title h2{font-family:"Oswald",Arial,sans-serif;font-weight:700;font-size:62px;text-transform:uppercase;letter-spacing:1px;line-height:1;padding:0 24px}
.section-title .rule{flex:1;height:8px}
.t-left h2{padding-left:40px}
.t-right h2{padding-right:40px}
.appetizers{top:395px}.appetizers h2{color:var(--orange)}.appetizers .rule{background:var(--orange);opacity:.35}
.salads{top:830px}.salads h2{color:var(--blue)}.salads .rule{background:var(--blue);opacity:.35}
.sandwiches{top:1180px}.sandwiches h2{color:var(--blue)}.sandwiches .rule{background:var(--blue);opacity:.35}
.mexican{top:1790px}.mexican h2{color:var(--red)}.mexican .rule{background:var(--red);opacity:.35}
.note{position:absolute;left:40px;top:1252px;font-size:19px;color:var(--muted)}
.items{position:absolute;left:40px;width:1120px;display:grid;grid-template-columns:1fr 1fr;column-gap:60px}
.col{display:flex;flex-direction:column;gap:10px}
.item{display:grid;grid-template-columns:1fr 70px;column-gap:10px}
.item h3{font-size:21px;font-weight:700;text-transform:uppercase;line-height:1.15}
.item p{grid-column:1;font-size:17px;color:var(--muted);line-height:1.2}
.item .price{grid-column:2;grid-row:1;text-align:right;font-size:21px;color:var(--orange);font-weight:400}
.item .extra{color:var(--orange)}
.app-items{top:480px}
.sal-items{top:912px}
.san-items{top:1292px}.san-items .col{gap:16px}
.mex-items{top:1872px}
.footer{position:absolute;left:0;top:2080px;width:1200px;height:176px;background:var(--navy);color:#ffffff;padding:26px 40px}
.footer .venue{font-family:"Oswald",Arial,sans-serif;font-weight:700;font-size:30px;color:var(--orange);margin-bottom:10px}
.contact{display:grid;grid-template-columns:340px 300px;row-gap:12px;font-size:19px}
.contact span{font-weight:700}
.social{display:flex;gap:8px;margin-top:6px}
.social i{display:block;width:26px;height:26px;background:var(--blue);border:2px solid #ffffff}
.callout{position:absolute;left:800px;top:2040px;width:350px;height:180px;background:#ffffff;border:3px solid var(--ink);transform:rotate(-4deg);display:flex;align-items:center;justify-content:center;padding:20px;text-align:center;font-family:"Kalam",cursive;font-size:31px;line-height:1.15;color:var(--ink)}
</style>
</head>
<body>
<main class="menu">
  <header class="header">
    <div class="wood" role="img" aria-label="Wooden plank background"></div>
    <div class="brand"><span class="name">Harrows</span><span class="sub">Grill</span></div>
  </header>

  <div class="section-title appetizers t-left"><h2>Appetizers</h2><div class="rule"></div></div>
  <section class="items app-items">
    <div class="col">
      <div class="item"><h3>Carrots and Celery</h3><span class="price">$00.0</span></div>
      <div class="item"><h3>Fresh Made Chips</h3><span class="price">$00.0</span><p>homemade salsa or guacamole</p></div>
      <div class="item"><h3>French Fries</h3><span class="price">$00.0</span></div>
      <div class="item"><h3>Chili Cheese Fries</h3><span class="price">$00.0</span></div>
      <div class="item"><h3>Onion Rings</h3><span class="price">$00.0</span></div>
      <div class="item"><h3>Mozzarella Sticks (6)</h3><span class="price">$00.0</span></div>
      <div class="item"><h3>Loaded Potato Skins (4)</h3><span class="price">$00.0</span></div>
      <div class="item"><h3>Harrows Jumbo Cut Wings</h3><span class="price">$00.0</span><p>buffalo, bbq or lemon pepper (8 or 12 pieces)</p></div>
    </div>
    <div class="col">
      <div class="item"><h3>Handmade Meatballs (4)</h3><span class="price">$00.0</span><p>ground beef / spices / marinara / garlic bread</p></div>
      <div class="item"><h3>Chicken Tenders</h3><span class="price">$00.0</span></div>
      <div class="item"><h3>Buffalo or Regular Fries</h3><span class="price">$00.0</span></div>
      <div class="item"><h3>Loaded Nachos</h3><span class="price">$00.0</span><p>chicken or asada / beans / sour cream / guacamole salsa / jalapeños</p></div>
      <div class="item"><h3>Harrows Sampler Platter</h3><span class="price">$00.0</span><p>4 buffalo wings / 4 mozzarella sticks / 4 potato skins 2 chicken tenders</p></div>
    </div>
  </section>

  <div class="section-title salads t-right"><div class="rule"></div><h2>Salads</h2></div>
  <section class="items sal-items">
    <div class="col">
      <div class="item"><h3>Harrows House Salad</h3><span class="price">$00.0</span><p>croutons / tomatoes / dressing</p></div>
      <div class="item"><h3>Caesar</h3><span class="price">$00.0</span><p>chicken / croutons / tossed in caesar dressing</p></div>
      <div class="item"><h3>The Country Cobb</h3><span class="price">$00.0</span><p>grilled chicken / bacon / chopped egg / blue cheese crumbles / baby heirloom / tomatoes / avocado / ranch dressing</p></div>
    </div>
    <div class="col">
      <div class="item"><h3>Grilled Chicken Salad</h3><span class="price">$00.0</span><p>chicken / avocado / tomatoes / croutons / dressing</p></div>
      <div class="item"><h3>Buffalo Chicken Salad</h3><span class="price">$00.0</span><p>celery / tomato / avocado / breaded chicken with buffalo sauce / blue cheese dressing</p></div>
      <div class="item"><h3>Balsamic Salad</h3><span class="price">$00.0</span><p>grilled chicken / bacon / blue cheese crumbles walnuts tomato / dried cranberries / balsamic vinaigrette</p></div>
    </div>
  </section>

  <div class="section-title sandwiches t-left"><h2>Sandwiches</h2><div class="rule"></div></div>
  <p class="note">served with french fries, sweet potato fries, onion rings or a small house salad.</p>
  <section class="items san-items">
    <div class="col">
      <div class="item"><h3>Grilled Chicken Chipotle</h3><span class="price">$00.0</span><p>pepper jack cheese / lettuce / tomato / brioche bun</p></div>
      <div class="item"><h3>Grilled Chicken Club</h3><span class="price">$00.0</span><p>bacon / lettuce / tomato / mayo / swiss cheese brioche bun</p></div>
      <div class="item"><h3>Hawaiian Chicken</h3><span class="price">$00.0</span><p>pineapple / grilled onions / teriyaki / swiss cheese brioche bun</p></div>
      <div class="item"><h3>Grilled Cheese</h3><span class="price">$00.0</span><p>texas toast / american / swiss</p></div>
      <div class="item"><h3>BBQ Grilled Cheese</h3><span class="price">$00.0</span><p>texas toast / bacon / american / swiss / bbq sauce</p></div>
      <div class="item"><h3>Patty Melt</h3><span class="price">$00.0</span><p>sourdough / swiss cheese / grilled onions</p></div>
    </div>
    <div class="col">
      <div class="item"><h3>Turkey</h3><span class="price">$00.0</span><p>all natural turkey / swiss / lettuce / tomato / pickle</p></div>
      <div class="item"><h3>Roast Beef Sandwich</h3><span class="price">$00.0</span><p>mayo / provolone cheese / lettuce / tomato brioche bun</p></div>
      <div class="item"><h3>Meatball</h3><span class="price">$00.0</span><p>homemade meatballs / mozzarella / marinara served on a french roll</p></div>
      <div class="item"><h3>French Dip</h3><span class="price">$00.0</span><p>choice angus top round / provolone / side of au jus served on a french roll</p></div>
      <div class="item"><h3>Bacon Bacon BLT</h3><span class="price">$00.0</span><p>bacon / bacon / more bacon / lettuce / tomato mayo / sourdough</p></div>
    </div>
  </section>

  <div class="section-title mexican t-right"><div class="rule"></div><h2>Mexican</h2></div>
  <section class="items mex-items">
    <div class="col">
      <div class="item"><h3>Chicken or Carnitas Tacos (3)</h3><span class="price">$00.0</span><p>lettuce / cheese / tomatoes / salsa</p></div>
      <div class="item"><h3>Asada Tacos (3)</h3><span class="price">$00.0</span><p>lettuce / cheese / tomatoes / salsa</p></div>
      <div class="item"><h3>Chicken or Carnitas Burritos</h3><span class="price">$00.0</span><p>beans / cheese / side of salsa <span class="extra">(wet add $1.50)</span></p></div>
    </div>
    <div class="col">
      <div class="item"><h3>Asada Burrito</h3><span class="price">$00.0</span><p>beans / cheese / side of salsa <span class="extra">(wet add $1.50)</span></p></div>
      <div class="item"><h3>Chicken Quesadilla</h3><span class="price">$00.0</span><p>salsa / sour cream</p></div>
      <div class="item"><h3>Asada Quesadilla</h3><span class="price">$00.0</span><p>salsa / sour cream</p></div>
    </div>
  </section>

  <footer class="footer">
    <div class="venue">Harrows Grill</div>
    <div class="contact">
      <div><span>address:</span></div>
      <div><span>email:</span></div>
      <div><span>phone:</span> (000) 000-0000</div>
      <div><span>web:</span><div class="social"><i></i><i></i><i></i><i></i></div></div>
    </div>
  </footer>
  <aside class="callout">Ask about our daily special, menu item, spotlight, or etc</aside>
</main>
</body>
</html>
```